The Ashcombe- outdoor banner

This should be a horizontal banner. It should have the logos attached incorporated and the following details
Coming Spring 2025: The Ashcombe - Exclusive Luxury Condos
Listed by Marisol Avenell | Quillfield Realty
Construction by Pinegate Builders
Unveil the height of luxury living with The Ashcombe, a new condo building in East Boston, set for completion in Spring 2025. Experience a standard of elegance and sophistication like never before.
For more information and inquiries, please contact:
Marisol Avenell
Phone: (617) 490-7163
Email: marisol@quillfieldhomes.example
The banner should be very classy incorporting gold and navy very classic fonts. The Ashcombe should look very classy and exclusive. The pinegate builders logo should be smaller. It should not include their phone number and instagram handle only the name of the company. Herringbone pattern in the background would be great. This is going outside the building to advertise pre construction units

```html
<!DOCTYPE html>
<html lang="en">
<head>
<meta charset="utf-8">
<title>The Ashcombe – Outdoor Banner</title>
<link rel="stylesheet" href="https://fonts.googleapis.com/css2?family=Montserrat:wght@500;600;700&family=DM+Serif+Display&family=Crimson+Pro:wght@400&family=Barlow+Condensed:wght@500&display=swap">
<style>
  :root {
    --navy-deep: #1b2238;
    --navy: #2a3a5f;
    --navy-band: #22304f;
    --gold: #e3b462;
    --gold-light: #f3dcae;
    --white: #ffffff;
    --page: #ffffff;
  }
  * { margin: 0; padding: 0; box-sizing: border-box; }
  html, body { width: 1200px; height: 999px; overflow: hidden; background: var(--page); }
  .canvas { position: relative; width: 1200px; height: 999px; }
  .banner {
    position: absolute; left: 0; top: 200px; width: 1200px; height: 600px;
    background: linear-gradient(160deg, var(--navy-deep) 0%, #253255 45%, var(--navy) 100%);
    overflow: hidden;
  }
  .banner__sweep {
    position: absolute; inset: 0;
    background: linear-gradient(115deg, transparent 55%, rgba(120,140,190,0.18) 56%, rgba(120,140,190,0.08) 80%, transparent 100%);
  }
  .banner__photo {
    position: absolute; left: 0; top: 380px; width: 1200px; height: 125px;
    background: linear-gradient(180deg, #3b4b72 0%, #4a5677 60%, #5b5570 100%);
  }
  .banner__lines { position: absolute; left: 0; top: 0; }
  .badge {
    position: absolute; top: 0; width: 86px; height: 98px;
    background: var(--white); border-radius: 0 0 43px 43px;
    display: flex; flex-direction: column; align-items: center; justify-content: center; gap: 6px;
    font-family: "Montserrat", sans-serif; font-weight: 700; font-size: 8px;
    color: var(--navy-band); text-align: center; line-height: 1.15; text-transform: uppercase;
  }
  .badge--builder { left: 45px; }
  .badge--realty { left: 1053px; color: #c9a25a; }
  .badge__dot { width: 18px; height: 18px; border-radius: 50%; background: currentColor; }
  .kicker {
    position: absolute; top: 46px; width: 100%; text-align: center;
    font-family: "Montserrat", sans-serif; font-weight: 600; font-size: 25px; color: var(--white);
  }
  .title {
    position: absolute; top: 86px; width: 100%; text-align: center;
    font-family: "DM Serif Display", serif; font-size: 84px; color: var(--gold); letter-spacing: -1px;
  }
  .subtitle {
    position: absolute; top: 196px; width: 100%; text-align: center;
    font-family: "Montserrat", sans-serif; font-weight: 600; font-size: 26px; color: var(--gold);
  }
  .intro {
    position: absolute; top: 252px; width: 100%; text-align: center;
    font-family: "Crimson Pro", serif; font-size: 26px; line-height: 33px; color: var(--white);
  }
  .credit {
    position: absolute; top: 425px;
    font-family: "Barlow Condensed", sans-serif; font-weight: 500; font-size: 27px; color: var(--gold);
  }
  .credit--listing { left: 59px; }
  .credit--builder { left: 725px; }
  .contact {
    position: absolute; left: 0; top: 505px; width: 1200px; height: 95px;
    background: var(--navy-band); color: var(--white);
    font-family: "Montserrat", sans-serif;
  }
  .contact__lead { position: absolute; left: 57px; top: 8px; font-weight: 600; font-size: 23px; }
  .contact__name { position: absolute; left: 52px; top: 42px; font-weight: 600; font-size: 34px; }
  .contact__item { position: absolute; top: 48px; display: flex; align-items: center; gap: 8px; font-weight: 600; font-size: 26px; }
  .contact__item--phone { left: 383px; }
  .contact__item--email { left: 660px; }
</style>
</head>
<body>
<div class="canvas">
  <section class="banner">
    <div class="banner__sweep"></div>
    <div class="banner__photo" role="img" aria-label="Photo of a two-storey home with gabled roof at dusk"></div>

    <svg class="banner__lines" width="1200" height="600" viewBox="0 0 1200 600" aria-hidden="true">
      <defs>
        <linearGradient id="goldLine" x1="0" x2="1" y1="0" y2="0">
          <stop offset="0" stop-color="#d9ad5e"/>
          <stop offset="0.5" stop-color="#f6e2b8"/>
          <stop offset="1" stop-color="#d9ad5e"/>
        </linearGradient>
      </defs>
      <rect x="0" y="10" width="1200" height="9" fill="url(#goldLine)"/>
      <path d="M0 354 H590 L668 385 H1200" fill="none" stroke="url(#goldLine)" stroke-width="7"/>
      <path d="M0 376 H590 L668 407 H1200" fill="none" stroke="url(#goldLine)" stroke-width="7"/>
    </svg>

    <div class="badge badge--builder"><span class="badge__dot"></span>Pinegate<br>Builders</div>
    <div class="badge badge--realty"><span class="badge__dot"></span>Quillfield<br>Realty</div>

    <p class="kicker">Coming Spring 2025:</p>
    <h1 class="title">The Ashcombe</h1>
    <p class="subtitle">- Exclusive Luxury Condos -</p>
    <p class="intro">Unveil the height of luxury living with The Ashcombe, a new condo building in East Boston,<br>set for completion in Spring 2025. Experience a standard of elegance and sophistication like never before.</p>

    <p class="credit credit--listing">Listed by Marisol Avenell | Quillfield Realty</p>
    <p class="credit credit--builder">Construction by Pinegate Builders</p>

    <div class="contact">
      <p class="contact__lead">For more information and inquiries, please contact:</p>
      <p class="contact__name">Marisol Avenell</p>
      <p class="contact__item contact__item--phone">
        <svg width="38" height="38" viewBox="0 0 38 38" aria-hidden="true">
          <circle cx="19" cy="19" r="17" fill="none" stroke="#fff" stroke-width="2.5"/>
          <path d="M12 11 l4 -1 l3 6 l-3 2 q2 5 6 7 l2 -3 l6 3 l-1 4 q-10 1 -17 -18z" fill="none" stroke="#fff" stroke-width="2.2" stroke-linejoin="round"/>
        </svg>(617) 490-7163
      </p>
      <p class="contact__item contact__item--email">
        <svg width="50" height="34" viewBox="0 0 50 34" aria-hidden="true">
          <rect x="2" y="2" width="46" height="30" fill="none" stroke="#fff" stroke-width="3"/>
          <path d="M2 2 L25 20 L48 2 M2 32 L19 16 M48 32 L31 16" fill="none" stroke="#fff" stroke-width="3"/>
        </svg>: marisol@quillfieldhomes.example
      </p>
    </div>
  </section>
</div>
</body>
</html>
```